A-Stand Directional Sign Design

Objective:
We need a professional graphic design for an A-Stand sign that will guide customers arriving in our parking lot to our office. The design should be visually clear, welcoming, and aligned with our brand identity.
REQUIREMENTS:
Two versions of the design:
- One with an arrow pointing left
- One with an arrow pointing right
(This allows us to place the A-Stand anywhere and flip the graphic as needed.)
DIMENSIONS:
- Viewable Area: 30" x 40"
BRAND ALIGNMENT:
- Colors, fonts, and overall style should match our website: www.glidecrest.com
- Clean, modern, and professional look consistent with our aviation/tourism brand
CONTENT:
- Clear directional arrow (left or right depending on version)
- Text: “Office Entrance” or similar concise wording (designers may propose alternatives if they improve clarity)
READABILITY:
- Bold, high-contrast design for visibility from a distance
- Simple layout that avoids clutter
DELIVERABLES:
- Final artwork in print-ready format (PDF preferred)
- Two versions: Arrow Left and Arrow Right
DESIGN GOAL:
Ensure customers can easily find our office upon arrival, while reinforcing glideCREST’s professional and welcoming brand image.
Target Market(s)
Tourism
Look and feel

```html
<!DOCTYPE html>
<html lang="en">
<head>
<meta charset="utf-8">
<title>glideCREST – Office Entrance A-Stand Signs</title>
<link rel="stylesheet" href="https://fonts.googleapis.com/css2?family=Anton&display=swap">
<style>
  :root {
    --page-bg: #d9d9d9;
    --sign-white: #ffffff;
    --sky-pale: #d8eaf7;
    --brand-blue: #2b74bb;
    --brand-blue-light: #86a9d6;
    --arrow-blue: #3364b4;
    --arrow-glow: #2a90d6;
    --accent-pink: #bf4a86;
    --desert-orange: #c98a45;
    --desert-light: #e8c08c;
    --sky-blue: #8fb3d8;
    --cloud: #e6e4df;
    --tarmac: #a58d6e;
    --tarmac-dark: #5b4a3a;
    --night: #050608;
  }
  * { margin: 0; padding: 0; box-sizing: border-box; }
  html, body { width: 980px; height: 1200px; overflow: hidden; }
  body {
    background: var(--page-bg);
    font-family: "Anton", "Arial Narrow", sans-serif;
    position: relative;
  }
  .sign {
    position: absolute;
    left: 151px;
    width: 678px;
    height: 510px;
    display: block;
  }
  .sign--left  { top: 69px; }
  .sign--right { top: 625px; }
  .sign__label {
    font-family: "Anton", "Arial Narrow", sans-serif;
    fill: var(--sign-white);
    font-size: 112px;
  }
  .sign__brand {
    font-family: "Anton", "Arial Narrow", sans-serif;
    fill: var(--brand-blue);
    font-size: 74px;
  }
</style>
</head>
<body>

<svg class="sign sign--left" viewBox="0 0 1202 902" aria-label="Office entrance sign, arrow pointing left">
  <defs>
    <linearGradient id="photoTones" x1="0" y1="0" x2="0" y2="1">
      <stop offset="0" stop-color="var(--sky-blue)"/>
      <stop offset="0.35" stop-color="var(--cloud)"/>
      <stop offset="0.6" stop-color="#cfc7bb"/>
      <stop offset="0.8" stop-color="var(--tarmac)"/>
      <stop offset="1" stop-color="var(--tarmac-dark)"/>
    </linearGradient>
    <linearGradient id="desertTones" x1="0" y1="0" x2="1" y2="1">
      <stop offset="0" stop-color="var(--desert-orange)"/>
      <stop offset="0.5" stop-color="var(--desert-light)"/>
      <stop offset="1" stop-color="#a8682d"/>
    </linearGradient>
    <linearGradient id="bandTones" x1="0" y1="0" x2="1" y2="0">
      <stop offset="0" stop-color="var(--arrow-blue)"/>
      <stop offset="0.55" stop-color="var(--arrow-glow)"/>
      <stop offset="1" stop-color="var(--arrow-blue)"/>
    </linearGradient>
  </defs>

  <g class="sign__artwork">
    <rect class="sign__base" width="1202" height="902" fill="var(--sign-white)"/>
    <polygon class="sign__sky-wedge" points="578,0 1018,0 793,162" fill="var(--sky-pale)"/>
    <polygon class="sign__photo" role="img" aria-label="Photo of a helicopter parked on a wet tarmac under a cloudy sky"
      points="1018,0 1202,0 1202,902 0,902 0,725 340,485 793,162" fill="url(#photoTones)"/>
    <polygon class="sign__photo-inset" role="img" aria-label="Photo of a helicopter flying over an orange desert haze"
      points="0,237 333,477 0,707" fill="url(#desertTones)"/>
    <polygon class="sign__stripe" points="1202,555 1202,575 735,902 705,902" fill="var(--sign-white)"/>
    <polygon class="sign__shadow-wedge" points="1202,580 1202,902 740,902" fill="var(--night)"/>
    <polygon class="sign__marker sign__marker--light" points="345,340 345,460 261,400" fill="var(--brand-blue-light)"/>
    <polygon class="sign__marker sign__marker--dark" points="360,382 360,454 410,418" fill="var(--brand-blue)"/>
    <polygon class="sign__marker sign__marker--pink" points="420,355 420,407 383,381" fill="var(--accent-pink)"/>
  </g>

  <g class="sign__arrow">
    <rect x="268" y="655" width="934" height="155" fill="url(#bandTones)"/>
    <polygon points="60,732 268,584 268,880" fill="var(--arrow-blue)"/>
  </g>
  <text class="sign__label" x="253" y="777" textLength="890" lengthAdjust="spacingAndGlyphs">OFFICE ENTRANCE</text>

  <g class="sign__brand-block">
    <circle cx="333" cy="150" r="42" fill="var(--brand-blue)"/>
    <text class="sign__brand" x="333" y="270" text-anchor="middle">glideCREST</text>
  </g>
</svg>

<svg class="sign sign--right" viewBox="0 0 1202 902" aria-label="Office entrance sign, arrow pointing right">
  <g class="sign__artwork" transform="translate(1202 0) scale(-1 1)">
    <rect class="sign__base" width="1202" height="902" fill="var(--sign-white)"/>
    <polygon class="sign__sky-wedge" points="578,0 1018,0 793,162" fill="var(--sky-pale)"/>
    <polygon class="sign__photo" role="img" aria-label="Photo of a helicopter parked on a wet tarmac under a cloudy sky"
      points="1018,0 1202,0 1202,902 0,902 0,725 340,485 793,162" fill="url(#photoTones)"/>
    <polygon class="sign__photo-inset" role="img" aria-label="Photo of a helicopter flying over an orange desert haze"
      points="0,237 333,477 0,707" fill="url(#desertTones)"/>
    <polygon class="sign__stripe" points="1202,555 1202,575 735,902 705,902" fill="var(--sign-white)"/>
    <polygon class="sign__shadow-wedge" points="1202,580 1202,902 740,902" fill="var(--night)"/>
    <polygon class="sign__marker sign__marker--light" points="345,340 345,460 261,400" fill="var(--brand-blue-light)"/>
    <polygon class="sign__marker sign__marker--dark" points="360,382 360,454 410,418" fill="var(--brand-blue)"/>
    <polygon class="sign__marker sign__marker--pink" points="420,355 420,407 383,381" fill="var(--accent-pink)"/>
  </g>

  <g class="sign__arrow">
    <rect x="0" y="655" width="934" height="155" fill="url(#bandTones)"/>
    <polygon points="1142,732 934,584 934,880" fill="var(--arrow-blue)"/>
  </g>
  <text class="sign__label" x="53" y="777" textLength="890" lengthAdjust="spacingAndGlyphs">OFFICE ENTRANCE</text>

  <g class="sign__brand-block">
    <circle cx="843" cy="150" r="42" fill="var(--brand-blue)"/>
    <text class="sign__brand" x="843" y="270" text-anchor="middle">glideCREST</text>
  </g>
</svg>

</body>
</html>
```